Eye catching Stationary Design

Healthcare consultant firm looking for stationary design ( letterhead, envelope and business cards) That’s professional, classy and eye catching . The design should incorporate the logo and the colors of the logo in its design. You can see the logo on our website at www crestmore advisory. net.

```html
<!DOCTYPE html>
<html lang="en">
<head>
<meta charset="utf-8">
<title>Crestmore Advisory Stationery</title>
<link rel="stylesheet" href="https://fonts.googleapis.com/css2?family=Nunito+Sans:wght@400;600;700&display=swap">
<style>
  :root {
    --brand-blue: #2466a3;
    --brand-blue-soft: #2f72a8;
    --brand-green: #5aab37;
    --ink: #4a4f55;
    --paper: #ffffff;
    --backdrop: #eceef0;
    --rule: #c9ced4;
  }
  * { box-sizing: border-box; margin: 0; padding: 0; }
  html, body { width: 1200px; height: 795px; overflow: hidden; }
  body {
    background: var(--backdrop);
    font-family: "Nunito Sans", Arial, sans-serif;
    color: var(--ink);
    position: relative;
  }
  .sheet {
    position: absolute;
    background: var(--paper);
    box-shadow: 0 2px 10px rgba(0,0,0,.12);
    overflow: hidden;
  }
  .wordmark {
    display: flex;
    align-items: center;
    gap: 8px;
    color: var(--brand-blue);
    font-weight: 600;
    letter-spacing: .12em;
    text-transform: uppercase;
    white-space: nowrap;
  }
  .wordmark .mark-square { background: var(--brand-green); flex: none; }
  .end-square { position: absolute; background: var(--brand-blue); }
  .contact-list { list-style: none; }
  .contact-list li { display: flex; align-items: center; gap: 5px; white-space: nowrap; }
  .contact-list svg { flex: none; fill: var(--brand-blue); }

  /* Letterhead */
  .letterhead { left: 40px; top: 40px; width: 480px; height: 715px; }
  .letterhead .wordmark { position: absolute; left: 48px; top: 56px; font-size: 22px; }
  .letterhead .wordmark .mark-square { width: 22px; height: 22px; }
  .letterhead .address {
    position: absolute; right: 36px; bottom: 80px;
    font-size: 9.5px; white-space: nowrap;
  }
  .letterhead .footer-contacts {
    position: absolute; right: 36px; bottom: 62px;
    display: flex; justify-content: flex-end; gap: 14px; font-size: 9.5px;
  }
  .letterhead .footer-bar { position: absolute; left: 0; right: 40px; bottom: 40px; height: 8px; background: var(--brand-blue); }
  .letterhead .end-square { right: 22px; bottom: 34px; width: 20px; height: 20px; background: var(--brand-green); }

  /* Envelope */
  .envelope { left: 570px; top: 40px; width: 590px; height: 300px; }
  .envelope .flap {
    position: absolute; left: 0; top: 0; width: 100%; height: 78px;
    background: var(--brand-blue);
    clip-path: polygon(4% 0, 96% 0, 100% 100%, 0 100%);
    display: flex; align-items: center; justify-content: center;
  }
  .envelope .flap .flap-square { width: 48px; height: 48px; background: var(--paper); }
  .envelope .wordmark { position: absolute; left: 24px; top: 104px; font-size: 19px; }
  .envelope .wordmark .mark-square { width: 20px; height: 20px; }
  .envelope .sender {
    position: absolute; right: 22px; top: 100px;
    display: flex; gap: 10px; font-size: 8.5px; line-height: 1.6;
  }
  .envelope .sender address { font-style: normal; padding-right: 10px; border-right: 1px solid var(--rule); align-self: center; }
  .envelope .footer-bar { position: absolute; left: 0; right: 34px; bottom: 16px; height: 7px; background: var(--brand-blue); }
  .envelope .end-square { right: 14px; bottom: 10px; width: 18px; height: 18px; background: var(--brand-green); }

  /* Business cards */
  .card { width: 285px; height: 165px; top: 400px; }
  .card-front { left: 570px; background: var(--brand-blue-soft); display: flex; align-items: center; justify-content: center; }
  .card-front .wordmark { color: var(--paper); font-size: 15px; }
  .card-front .wordmark .mark-square { width: 14px; height: 14px; background: var(--paper); }
  .card-back { left: 875px; }
  .card-back .wordmark { position: absolute; left: 18px; top: 20px; font-size: 12px; }
  .card-back .wordmark .mark-square { width: 12px; height: 12px; }
  .card-back .holder { position: absolute; left: 18px; top: 62px; font-size: 7.5px; line-height: 1.5; padding-right: 12px; border-right: 1px solid var(--rule); }
  .card-back .holder-name { color: var(--brand-blue); font-weight: 700; font-size: 9.5px; }
  .card-back .holder address { font-style: normal; margin-top: 4px; }
  .card-back .contact-list { position: absolute; left: 150px; top: 66px; font-size: 7.5px; line-height: 1.9; }
  .card-back .footer-bar { position: absolute; left: 0; right: 26px; bottom: 18px; height: 6px; background: var(--brand-blue); }
  .card-back .end-square { right: 10px; bottom: 13px; width: 14px; height: 14px; background: var(--brand-green); }
</style>
</head>
<body>
<svg width="0" height="0" style="position:absolute">
  <defs>
    <symbol id="icon-phone" viewBox="0 0 16 16"><circle cx="8" cy="8" r="7.5" fill="none" stroke="currentColor" stroke-width="1.4"/><path d="M5.2 4.2l1.6-.2.8 2-1 .8a5 5 0 0 0 2.6 2.6l.8-1 2 .8-.2 1.6c-3.6.4-7-3-6.6-6.6z"/></symbol>
    <symbol id="icon-mail" viewBox="0 0 16 16"><path d="M1 3h14v10H1z"/><path d="M1 3l7 6 7-6" fill="none" stroke="#fff" stroke-width="1.3"/></symbol>
    <symbol id="icon-web" viewBox="0 0 16 16"><circle cx="8" cy="8" r="7" fill="none" stroke="#2466a3" stroke-width="1.3"/><ellipse cx="8" cy="8" rx="3" ry="7" fill="none" stroke="#2466a3" stroke-width="1.1"/><path d="M1 8h14" stroke="#2466a3" stroke-width="1.1"/></symbol>
  </defs>
</svg>

<section class="sheet letterhead" aria-label="Letterhead">
  <div class="wordmark"><span class="mark-square"></span>Crestmore Advisory</div>
  <p class="address">40 Harlow Park Way Fairview, MN 55012</p>
  <ul class="contact-list footer-contacts">
    <li><svg width="10" height="10" style="color:#2466a3"><use href="#icon-phone"/></svg>555-014-2290</li>
    <li><svg width="10" height="10"><use href="#icon-mail"/></svg>info@crestmoreadvisory.net</li>
    <li><svg width="10" height="10"><use href="#icon-web"/></svg>www.crestmoreadvisory.net</li>
  </ul>
  <div class="footer-bar"></div>
  <div class="end-square"></div>
</section>

<section class="sheet envelope" aria-label="Envelope">
  <div class="flap"><span class="flap-square"></span></div>
  <div class="wordmark"><span class="mark-square"></span>Crestmore Advisory</div>
  <div class="sender">
    <address>40 Harlow Park Way<br>Fairview, MN 55012</address>
    <ul class="contact-list">
      <li><svg width="9" height="9" style="color:#2466a3"><use href="#icon-phone"/></svg>555-014-2290</li>
      <li><svg width="9" height="9"><use href="#icon-mail"/></svg>info@crestmoreadvisory.net</li>
      <li><svg width="9" height="9"><use href="#icon-web"/></svg>www.crestmoreadvisory.net</li>
    </ul>
  </div>
  <div class="footer-bar"></div>
  <div class="end-square"></div>
</section>

<section class="sheet card card-front" aria-label="Business card front">
  <div class="wordmark"><span class="mark-square"></span>Crestmore Advisory</div>
</section>

<section class="sheet card card-back" aria-label="Business card back">
  <div class="wordmark"><span class="mark-square"></span>Crestmore Advisory</div>
  <div class="holder">
    <p class="holder-name">Elena Marsh</p>
    <p>Chief Financial Officer</p>
    <address>40 Harlow Park Way<br>Fairview, MN 55012</address>
  </div>
  <ul class="contact-list">
    <li><svg width="8" height="8" style="color:#2466a3"><use href="#icon-phone"/></svg>555-014-2290</li>
    <li><svg width="8" height="8"><use href="#icon-mail"/></svg>info@crestmoreadvisory.net</li>
    <li><svg width="8" height="8"><use href="#icon-web"/></svg>www.crestmoreadvisory.net</li>
  </ul>
  <div class="footer-bar"></div>
  <div class="end-square"></div>
</section>
</body>
</html>
```